Website redesign

Looking to redesign our existing website. (hire4ward.com.au)
New design needs to be bright, fun and have an easy flowing.
The website needs to be design with call to action.

Some examples of other websites:
brightdesk.com
lendnest.com.au

We are happy with the content of our existing website.

Target Market(s)

other businesses

Industry/Entity Type

Business Service

Number of Pages Required

5+ page

Requirements
Must have
• Theme redesign
Cool animation similar to brightdesk.com

```html
<!DOCTYPE html>
<html lang="en">
<head>
<meta charset="utf-8">
<title>Hire4ward – Virtual Assistants</title>
<link href="https://fonts.googleapis.com/css2?family=Rubik:wght@400;500;700&family=Roboto:wght@400;500&display=swap" rel="stylesheet">
<style>
:root{
  --blue:#12a4df;
  --blue-dark:#0b8fc6;
  --ink:#1b1d22;
  --muted:#555b63;
  --hero-bg:#e7f8fd;
  --grey-bg:#f4f4f4;
  --quote-bg:#f8f8f8;
  --footer:#141e2b;
  --white:#ffffff;
}
*{box-sizing:border-box;margin:0;padding:0}
html,body{width:1200px;height:3715px;overflow:hidden}
body{font-family:"Roboto",sans-serif;color:var(--ink);background:var(--white);position:relative}
section,header,footer{position:relative;width:1200px}
.abs{position:absolute}

/* hero */
.hero{height:598px;background:var(--hero-bg)}
.brand{left:183px;top:26px;font-family:"Rubik",sans-serif;font-weight:700;font-size:30px;color:var(--ink);display:flex;align-items:center;gap:8px;z-index:2}
.brand .dot{width:14px;height:14px;border-radius:50%;background:var(--blue)}
.call{left:428px;top:34px;font-size:13px;font-weight:500;display:flex;align-items:center;gap:6px;z-index:2}
.call b{color:var(--blue);font-weight:500}
.nav{left:637px;top:29px;display:flex;align-items:center;z-index:2}
.nav a{font-size:10.5px;font-weight:500;text-decoration:none;color:var(--ink);padding:0 9px;line-height:30px}
.nav a.active{background:var(--blue);color:#fff;padding:0 16px;margin-right:4px}
.hero-copy{left:183px;top:236px;width:360px;z-index:2}
.hero-title{font-family:"Rubik",sans-serif;font-size:30px;line-height:34px;white-space:nowrap}
.hero-title .q{color:var(--blue);font-weight:500;display:block}
.hero-title .a{color:var(--ink);font-weight:400;display:block}
.hero-sub{font-size:12px;margin-top:12px;white-space:nowrap}
.btn{background:var(--blue);color:#fff;font-size:12.5px;display:flex;align-items:center;justify-content:center;border-radius:2px}
.hero-btn{width:114px;height:42px;margin-top:22px}
.hero-art{left:560px;top:95px;width:600px;height:503px;z-index:1;background:radial-gradient(ellipse at 50% 45%,#c9c2b8 0,#d8e6ea 30%,#e7f8fd 70%)}

/* outsourcing */
.outsource{height:412px}
.video{left:183px;top:75px;width:408px;height:257px;background:linear-gradient(135deg,#e9e5dc,#b9b2a6 45%,#6c5b4c 100%);overflow:hidden}
.video .bar{position:absolute;left:10px;right:10px;bottom:8px;height:26px;background:rgba(0,0,0,.55);display:flex;align-items:center;padding:0 10px;gap:12px}
.video .track{flex:1;height:5px;background:rgba(255,255,255,.3);position:relative}
.video .track i{position:absolute;left:0;top:0;height:5px;width:35%;background:var(--blue)}
.h-big{font-family:"Rubik",sans-serif;font-weight:700;color:var(--blue);font-size:42px;letter-spacing:.5px}
.out-copy{left:639px;top:92px}
.out-sub{font-family:"Rubik",sans-serif;font-size:23px;line-height:28px;font-weight:400;margin-top:4px}
.out-text{font-size:11.5px;line-height:24.5px;color:var(--muted);margin-top:22px;width:372px}

/* process */
.process{height:1221px;background:var(--grey-bg)}
.proc-title{left:523px;top:88px;font-family:"Rubik",sans-serif;line-height:1;z-index:2}
.proc-title .the{font-size:27px;font-weight:500;color:var(--ink);display:block}
.proc-title .word{font-size:38px;font-weight:700;color:var(--blue);display:block}
.spine{left:597px;top:144px;width:6px;height:920px;background:var(--blue)}
.node{width:60px;height:60px;border-radius:50%;background:var(--blue);left:570px;display:flex;align-items:center;justify-content:center;box-shadow:0 0 0 4px var(--grey-bg)}
.step{height:52px;background:#fff;font-family:"Rubik",sans-serif;font-weight:500;font-size:16px;display:flex;align-items:center;justify-content:center;box-shadow:0 3px 10px rgba(0,0,0,.08)}
.step.l{left:456px;width:92px;border-left:3px solid var(--ink)}
.step.r{left:650px;width:95px;border-right:3px solid var(--ink)}
.card{background:#fff;padding:24px 26px;box-shadow:0 4px 16px rgba(0,0,0,.07);border-radius:3px}
.card.r{left:650px;width:378px;border-right:3px solid var(--blue)}
.card.l{left:173px;width:378px;border-left:3px solid var(--blue)}
.card h3{font-family:"Rubik",sans-serif;color:var(--blue);font-size:16.5px;font-weight:500;margin-bottom:10px}
.card p{font-size:9.6px;line-height:17.5px;color:var(--muted)}

/* services */
.services{height:571px}
.center{left:0;width:1200px;text-align:center}
.svc-sub{font-size:12.5px;line-height:22px}
.svc{top:193px;width:193px;height:146px;border-radius:2px;padding:28px 24px 0;color:#fff;box-shadow:0 6px 14px rgba(0,0,0,.2)}
.svc.blue{background:linear-gradient(135deg,#19b8ee,#0b92c8)}
.svc.dark{background:linear-gradient(135deg,#4a4a4a,#222)}
.svc p{font-size:10px;line-height:14.5px;margin-top:18px}
.simple{font-family:"Rubik",sans-serif;font-weight:500;color:var(--blue);font-size:37px}
.simple-sub{font-family:"Rubik",sans-serif;font-size:16px;line-height:23px;font-weight:500}

/* quote */
.quote{height:604px;background:var(--quote-bg)}
.q-title{font-family:"Rubik",sans-serif;font-weight:700;color:var(--blue);font-size:34px}
.q-panel{left:0;top:202px;width:464px;height:298px;background:var(--blue);border-top-right-radius:26px;color:#fff;padding:48px 0 0 183px}
.q-panel h4{font-family:"Rubik",sans-serif;font-weight:700;font-size:18px}
.q-panel small{display:block;font-size:10.5px;margin-top:5px}
.q-panel ul{list-style:none;margin-top:16px}
.q-panel li{font-size:11.5px;line-height:24.5px;display:flex;align-items:center;gap:6px}
.field{background:#fff;border:1px solid #dcdcdc;font-size:9px;color:#9a9a9a;padding:0 11px;display:flex;align-items:center}
.field.area{align-items:flex-start;padding-top:12px}
.hint{left:505px;top:434px;font-size:8.5px;color:#555}
.robot{left:505px;top:453px;width:168px;height:39px;background:#f9f9f9;border:1px solid #d5d5d5;display:flex;align-items:center;padding:0 8px;gap:8px;font-size:8.5px}
.robot .box{width:14px;height:14px;border:2px solid #c1c1c1;background:#fff}
.robot .mk{margin-left:auto;width:18px;height:18px;background:#9eb6d8;border-radius:3px}
.submit{left:733px;top:453px;width:113px;height:39px;font-size:13px;font-weight:500}
.q-photo{left:880px;top:46px;width:320px;height:512px;background:radial-gradient(ellipse at 40% 55%,#6b6d72 0,#b9bbbf 35%,#ececec 70%,#f8f8f8 100%)}

/* footer */
.footer{height:309px;background:var(--footer);color:#fff}
.f-brand{font-family:"Rubik",sans-serif;font-weight:700;font-size:20px;top:60px}
.f-name{font-size:10.5px;top:88px;font-weight:500}
.f-sub{top:128px;color:var(--blue);font-size:12.5px;letter-spacing:.5px}
.f-form{left:454px;top:156px;width:292px;height:30px;display:flex}
.f-form span{flex:1;background:#fff;color:#8a8a8a;font-size:8.5px;display:flex;align-items:center;padding:0 14px}
.f-form b{width:34px;background:var(--blue);display:flex;align-items:center;justify-content:center}
.f-tag{top:212px;font-size:11px;font-weight:500}
.f-copy{top:232px;font-size:6.5px;color:#8d96a3;letter-spacing:.3px}
.to-top{left:584px;top:276px;width:33px;height:33px;background:var(--blue);display:flex;align-items:center;justify-content:center}
</style>
</head>
<body>

<header class="hero">
  <div class="abs brand">Hire4ward <span class="dot"></span></div>
  <div class="abs call">
    <svg width="13" height="13" viewBox="0 0 24 24"><path d="M6.6 10.8a15.1 15.1 0 0 0 6.6 6.6l2.2-2.2a1 1 0 0 1 1-.25 11.4 11.4 0 0 0 3.6.57 1 1 0 0 1 1 1V20a1 1 0 0 1-1 1A17 17 0 0 1 3 4a1 1 0 0 1 1-1h3.5a1 1 0 0 1 1 1c0 1.25.2 2.45.57 3.57a1 1 0 0 1-.25 1z" fill="#1b1d22"/></svg>
    Call Us <b>07 5550 1842</b>
  </div>
  <nav class="abs nav">
    <a class="active">HOME</a><a>OUR STORY</a><a>TIPS AND TRICKS</a><a>CONTACT US</a><a>FAQ</a>
  </nav>
  <div class="abs hero-art" role="img" aria-label="Smiling businesswoman with arms crossed, surrounded by hand-drawn blue doodles of communication, social media, growth and marketing icons"></div>
  <div class="abs hero-copy">
    <h1 class="hero-title"><span class="q">Virtual Assistant?</span><span class="a">More like valuable asset!</span></h1>
    <p class="hero-sub">Tech nerds on standby for setup, support and comms!</p>
    <div class="btn hero-btn">Get a Quote</div>
  </div>
</header>

<section class="outsource">
  <div class="abs video" role="img" aria-label="Video still of a business team meeting around a table, viewed from above">
    <div class="bar">
      <svg width="12" height="12" viewBox="0 0 12 12"><path d="M2 1l9 5-9 5z" fill="#fff"/></svg>
      <div class="track"><i></i></div>
      <span style="color:#fff;font-size:9px;font-weight:500">HD</span>
    </div>
  </div>
  <div class="abs out-copy">
    <h2 class="h-big">OUTSOURCING</h2>
    <p class="out-sub">A big word that means big things<br>for your business.</p>
    <p class="out-text">Virtual Assistants are the superheroes of the modern office. They can do everything your team can do on a computer at a fraction of the price! (Well, maybe not high five you when you've had a win, but a virtual high five is definitely on the table!)</p>
  </div>
</section>

<section class="process">
  <div class="abs spine"></div>
  <h2 class="abs proc-title"><span class="the">The</span><span class="word">PROCESS</span></h2>

  <div class="abs step l" style="top:252px">Step 1</div>
  <div class="abs node" style="top:248px"><svg width="26" height="20" viewBox="0 0 26 20"><path d="M3 10l7 7L23 3" fill="none" stroke="#fff" stroke-width="4" stroke-linecap="round" stroke-linejoin="round"/></svg></div>
  <div class="abs card r" style="top:204px;height:149px">
    <h3>Provide Your Preferred Qualifications</h3>
    <p>Set up a call with our team to specify the requirements and qualifications you're searching for in a Virtual Assistant. This will be our checklist for your perfect assistant! From there, we'll take care of shortlisting, testing, background checking and recruiting.</p>
  </div>

  <div class="abs card l" style="top:389px;height:151px">
    <h3>Endorsing the Shortlisted Candidates</h3>
    <p>After the thorough vetting process, we'll put forward the best candidate. You can then conduct the final interview on your preferred communication platform at a time that suits you. Once the schedule is set, we'll let the candidates know!</p>
  </div>
  <div class="abs node" style="top:434px"><svg width="26" height="20" viewBox="0 0 26 20"><path d="M3 10l7 7L23 3" fill="none" stroke="#fff" stroke-width="4" stroke-linecap="round" stroke-linejoin="round"/></svg></div>
  <div class="abs step r" style="top:438px">Step 2</div>

  <div class="abs step l" style="top:624px">Step 3</div>
  <div class="abs node" style="top:620px"><svg width="26" height="20" viewBox="0 0 26 20"><path d="M3 10l7 7L23 3" fill="none" stroke="#fff" stroke-width="4" stroke-linecap="round" stroke-linejoin="round"/></svg></div>
  <div class="abs card r" style="top:583px;height:135px">
    <h3>Conducting the Final Interview</h3>
    <p>The final interview is the perfect time to get to know the candidates. It'll help to have a list of questions prepared that will help you pick out the chosen one!</p>
  </div>

  <div class="abs card l" style="top:770px;height:131px">
    <h3>Setting up the Tools</h3>
    <p>Once you've chosen your Virtual Assistant, it's time for their system to be set up. You can get your own IT team onto the installation, otherwise, we've got a super team of tech peeps who can do it for you.</p>
  </div>
  <div class="abs node" style="top:806px"><svg width="26" height="20" viewBox="0 0 26 20"><path d="M3 10l7 7L23 3" fill="none" stroke="#fff" stroke-width="4" stroke-linecap="round" stroke-linejoin="round"/></svg></div>
  <div class="abs step r" style="top:810px">Step 4</div>

  <div class="abs step l" style="top:996px">Step 5</div>
  <div class="abs node" style="top:992px"><svg width="26" height="20" viewBox="0 0 26 20"><path d="M3 10l7 7L23 3" fill="none" stroke="#fff" stroke-width="4" stroke-linecap="round" stroke-linejoin="round"/></svg></div>
  <div class="abs card r" style="top:940px;height:170px">
    <h3>Your Magical Journey Begins</h3>
    <p>Now you and your Virtual Assistant are all set up and ready to rumble! Feel the magic of having a reliable assistant to take on all the menial, repetitive, time-consuming tasks, and focus your energy on more important things. Meet new clients, explore business opportunities, or just spend some time with friends and family!</p>
  </div>
</section>

<section class="services">
  <h2 class="abs center h-big" style="top:78px;font-size:34px">OUR SERVICES</h2>
  <p class="abs center svc-sub" style="top:128px">We'll help you save tens (or even hundreds!) of thousands of dollars per year. But what do WE actually do?<br>GLAD YOU ASKED!</p>

  <div class="abs svc blue" style="left:183px">
    <svg width="44" height="40" viewBox="0 0 44 40" fill="none" stroke="#fff" stroke-width="1.6"><rect x="6" y="3" width="32" height="24" rx="1"/><path d="M2 33h40l-3-6H5z"/><circle cx="22" cy="12" r="4"/><path d="M15 23c1-4 4-6 7-6s6 2 7 6"/></svg>
    <p>We recruit Virtual Assistants<br>(a.k.a office legends!)</p>
  </div>
  <div class="abs svc dark" style="left:397px">
    <svg width="44" height="40" viewBox="0 0 44 40" fill="none" stroke="#fff" stroke-width="1.6"><rect x="4" y="3" width="36" height="30" rx="1"/><path d="M4 10h36"/><circle cx="26" cy="22" r="6"/><path d="M9 16h8M9 21h6M9 26h8"/></svg>
    <p>Provide the tech support for<br>these superheroes!</p>
  </div>
  <div class="abs svc dark" style="left:610px">
    <svg width="44" height="40" viewBox="0 0 44 40" fill="none" stroke="#fff" stroke-width="1.6"><rect x="12" y="2" width="20" height="34" rx="3"/><path d="M18 6h8"/><circle cx="22" cy="19" r="6"/><path d="M19 19h6M22 16v6"/></svg>
    <p>Set up the phone system<br>(their own Hero Hotline!)</p>
  </div>
  <div class="abs svc dark" style="left:823px">
    <svg width="44" height="40" viewBox="0 0 44 40" fill="none" stroke="#fff" stroke-width="1.6"><rect x="6" y="8" width="32" height="22" rx="1"/><path d="M2 35h40l-3-5H5z"/><circle cx="22" cy="8" r="5"/><path d="M14 20h16M14 25h10"/></svg>
    <p>We manage Virtual Assistants<br>and keep them in tip-top shape!</p>
  </div>

  <h2 class="abs center simple" style="top:386px">See? It's that simple!</h2>
  <p class="abs center simple-sub" style="top:440px">The only thing to do now is to finally get started on the quote...<br>just scroll down a little more.</p>
</section>

<section class="quote">
  <h2 class="abs q-title" style="left:0;width:1172px;text-align:center;top:76px">GET A QUOTE</h2>
  <p class="abs" style="left:0;width:1172px;text-align:center;top:126px;font-size:12.5px">Fill in the form below to get a Quote for your own personal Virtual Assistant</p>

  <div class="abs q-panel">
    <h4>IT'S TIME TO OUTSOURCE</h4>
    <small>Why are we your new best outsourcing friend?</small>
    <ul>
      <li><svg width="11" height="9" viewBox="0 0 11 9"><path d="M1 4.5l3 3L10 1" fill="none" stroke="#fff" stroke-width="2"/></svg>Your Own Virtual Assistant</li>
      <li><svg width="11" height="9" viewBox="0 0 11 9"><path d="M1 4.5l3 3L10 1" fill="none" stroke="#fff" stroke-width="2"/></svg>One Invoice Per Month</li>
      <li><svg width="11" height="9" viewBox="0 0 11 9"><path d="M1 4.5l3 3L10 1" fill="none" stroke="#fff" stroke-width="2"/></svg>No Super or TAX</li>
      <li><svg width="11" height="9" viewBox="0 0 11 9"><path d="M1 4.5l3 3L10 1" fill="none" stroke="#fff" stroke-width="2"/></svg>Dedicated To Your Business Only</li>
      <li><svg width="11" height="9" viewBox="0 0 11 9"><path d="M1 4.5l3 3L10 1" fill="none" stroke="#fff" stroke-width="2"/></svg>Dedicated Phone System</li>
      <li><svg width="11" height="9" viewBox="0 0 11 9"><path d="M1 4.5l3 3L10 1" fill="none" stroke="#fff" stroke-width="2"/></svg>IT Setup and Support</li>
    </ul>
  </div>

  <div class="abs field" style="left:505px;top:203px;width:341px;height:29px">Business Name</div>
  <div class="abs field" style="left:505px;top:245px;width:165px;height:29px">First Name</div>
  <div class="abs field" style="left:681px;top:245px;width:165px;height:29px">Last Name</div>
  <div class="abs field" style="left:505px;top:287px;width:165px;height:29px">Phone</div>
  <div class="abs field" style="left:681px;top:287px;width:165px;height:29px">Email</div>
  <div class="abs field area" style="left:505px;top:329px;width:341px;height:86px">Describe the tasks you'll need from your Virtual Assistant</div>
  <p class="abs hint">Please check the box below to proceed.</p>
  <div class="abs robot"><span class="box"></span>I'm not a robot<span class="mk"></span></div>
  <div class="abs btn submit">Submit</div>

  <div class="abs q-photo" role="img" aria-label="Top-down desk scene with hands typing on a laptop, a potted succulent, coffee cup, pen, phone and binder clips"></div>
</section>

<footer class="footer">
  <div class="abs center f-brand">Hire4ward</div>
  <div class="abs center f-name">HIRE4WARD</div>
  <div class="abs center f-sub">Subscribe our Newsletter</div>
  <div class="abs f-form"><span>Enter your email here!</span><b><svg width="12" height="10" viewBox="0 0 12 10"><path d="M1 5h9M6 1l4 4-4 4" fill="none" stroke="#fff" stroke-width="1.6"/></svg></b></div>
  <div class="abs center f-tag">Virtual Assistant? More Like Valuable Asset!</div>
  <div class="abs center f-copy">© 2020 HIRE4WARD | ALL RIGHTS RESERVED</div>
  <div class="abs to-top"><svg width="12" height="12" viewBox="0 0 12 12"><path d="M6 11V2M2 6l4-4 4 4" fill="none" stroke="#fff" stroke-width="1.6"/></svg></div>
</footer>

</body>
</html>
```